Animal Eye Clinic needs a Business card

We are a new veterinary ophthalmology practice (Tessaly Animal Eye Care) and we need a business card designed. We only see animal eyes - we are not a regular veterinary clinic. We already have a logo. We are looking for a professional, good looking business card to hand out to our clients. We are looking for something simple but professional and contemporary. Our logo is likely the only picture/graphic that needs to be on the card.
Updates

Contact Information for Business Card

Marisol Dunkley, BSc, DVM, MSc, DipACVO
Veterinary Ophthalmologist

Phone: 250.418.3097
Email: tessalyanimaleyecare@mailbrook.net
Website: tessalyanimaleyecare.net
Address: 1840 Pellworth Rd
Kelowna, BC, V4T 8M3

Colors

Designer to choose colors to be used in the design.

Requirements
Must have
• Our logo (attached)

```html
<!DOCTYPE html>
<html lang="en">
<head>
<meta charset="utf-8">
<title>Tessaly Animal Eye Care – Business Card</title>
<link href="https://fonts.googleapis.com/css2?family=Open+Sans:wght@400;600;700&display=swap" rel="stylesheet">
<style>
  :root {
    --teal: #0399a9;
    --grey: #767676;
    --white: #ffffff;
    --backdrop: #d9d9d9;
    --shadow: rgba(0,0,0,0.35);
  }
  * { margin: 0; padding: 0; box-sizing: border-box; }
  html, body { width: 1200px; height: 802px; overflow: hidden; }
  body {
    background: var(--backdrop);
    font-family: "Open Sans", Arial, sans-serif;
    position: relative;
  }
  .card {
    position: absolute;
    top: 274px;
    width: 442px;
    height: 265px;
    box-shadow: 2px 3px 6px var(--shadow);
    overflow: hidden;
  }
  .card-front { left: 136px; background: var(--teal); color: var(--white); }
  .card-back { left: 624px; background: var(--white); }

  .front-art { position: absolute; inset: 0; }

  .identity { position: absolute; left: 19px; top: 30px; }
  .identity .name { font-weight: 700; font-size: 14px; letter-spacing: 0.2px; }
  .identity .credentials,
  .identity .role { font-size: 10.5px; line-height: 16px; }
  .identity .name + .credentials { margin-top: 1px; }

  .address { position: absolute; left: 19px; top: 144px; font-size: 10.5px; line-height: 16px; }

  .contact { position: absolute; left: 19px; top: 191px; list-style: none; font-size: 10.5px; line-height: 16px; }
  .contact li { display: flex; align-items: center; gap: 4px; white-space: nowrap; }
  .contact svg { width: 9px; height: 9px; flex: none; }

  .brand {
    position: absolute; left: 0; right: 0; top: 50%;
    transform: translateY(-50%);
    display: flex; align-items: center; justify-content: center; gap: 10px;
  }
  .brand-dot { width: 26px; height: 26px; border-radius: 50%; background: var(--teal); }
  .brand-name { color: var(--teal); font-weight: 600; font-size: 22px; letter-spacing: 0.2px; }
</style>
</head>
<body>
  <section class="card card-front">
    <svg class="front-art" viewBox="0 0 442 265" role="img" aria-label="Illustration of horse, dog and cat silhouettes in a white circle">
      <defs>
        <linearGradient id="artTone" x1="0" y1="0" x2="1" y2="1">
          <stop offset="0" stop-color="#ffffff"/>
          <stop offset="1" stop-color="#c4c4c4"/>
        </linearGradient>
      </defs>
      <polygon points="292,265 292,200 442,200 442,265" fill="var(--grey)"/>
      <polygon points="400,0 442,0 442,60" fill="var(--grey)"/>
      <circle cx="343" cy="132" r="138" fill="url(#artTone)"/>
    </svg>

    <div class="identity">
      <p class="name">MARISOL DUNKLEY</p>
      <p class="credentials">BSC, DVM, MSC, DIPACVO</p>
      <p class="role">Veterinary Ophthalmologist</p>
    </div>

    <address class="address" style="font-style:normal">
      1840 Pellworth Rd<br>
      Kelowna, BC, V4T 8M3
    </address>

    <ul class="contact">
      <li>
        <svg viewBox="0 0 10 10" aria-hidden="true"><path d="M1 3.5C1 2 2.5 1.5 5 1.5S9 2 9 3.5L7.5 4 7 3H3L2.5 4ZM2.5 5h5l1 3.5h-7Z" fill="currentColor"/></svg>
        250.418.3097
      </li>
      <li>
        <svg viewBox="0 0 10 10" aria-hidden="true"><rect x="0.5" y="2" width="9" height="6.5" fill="currentColor"/><path d="M0.8 2.3L5 5.6 9.2 2.3" stroke="var(--teal)" stroke-width="0.9" fill="none"/></svg>
        tessalyanimaleyecare@mailbrook.net
      </li>
      <li>
        <svg viewBox="0 0 10 10" aria-hidden="true"><circle cx="5" cy="5" r="4.5" fill="currentColor"/><path d="M3 3.5h2.5l-1 2 1.5 1.5-1 1.5" stroke="var(--teal)" stroke-width="0.9" fill="none"/></svg>
        tessalyanimaleyecare.net
      </li>
    </ul>
  </section>

  <section class="card card-back">
    <div class="brand">
      <span class="brand-dot" aria-hidden="true"></span>
      <span class="brand-name">Tessaly Animal Eye Care</span>
    </div>
  </section>
</body>
</html>
```